Burn Cream

We need to develop a (1) tube and (2) carton design. For a Lidocaine 2.5% burn cream.

This is a topical application cream. KALVIO is the Product Name. 1 oz.

```html
<!DOCTYPE html>
<html lang="en">
<head>
<meta charset="utf-8">
<title>Kalvio Burn Cream – Tube Labels</title>
<link rel="stylesheet" href="https://fonts.googleapis.com/css2?family=Josefin+Sans:wght@300;400&display=swap">
<style>
  :root {
    --bg: #ffffff;
    --tube-dark: #121414;
    --tube-mid: #2a2e2e;
    --cap: #0c0d0d;
    --silver: #d9dcdc;
    --text: #e9ecec;
    --flame-red: #e8321a;
    --flame-orange: #f7821e;
    --flame-yellow: #ffc83a;
  }
  * { margin: 0; padding: 0; box-sizing: border-box; }
  html, body {
    width: 1200px; height: 1200px; overflow: hidden;
    background: var(--bg);
    font-family: "Josefin Sans", sans-serif;
  }
  .canvas { position: relative; width: 1200px; height: 1200px; }

  .tube {
    position: absolute; top: 42px; height: 1116px;
    overflow: hidden;
    background: linear-gradient(90deg, var(--tube-dark) 0%, var(--tube-mid) 14%, var(--tube-dark) 40%, var(--tube-dark) 100%);
  }
  .tube--front { left: 156px; width: 372px; }
  .tube--side { left: 648px; width: 384px; }

  .crimp {
    position: absolute; top: 0; left: 0; right: 0; height: 16px;
    background: repeating-linear-gradient(90deg, #1b1d1d 0 2px, #0a0b0b 2px 4px);
  }
  .silver-band {
    position: absolute; left: 0; right: 0; top: 906px; height: 6px;
    background: linear-gradient(90deg, #8c9090, var(--silver) 30%, #ffffff 50%, var(--silver) 70%, #8c9090);
  }
  .cap {
    position: absolute; left: 0; right: 0; top: 918px; bottom: 0;
    background: linear-gradient(90deg, var(--cap), #1e2020 18%, var(--cap) 45%);
  }

  .flame { position: absolute; }
  .tube--front .flame--edge {
    right: 0; top: 16px; width: 170px; height: 890px;
    background:
      radial-gradient(ellipse 60% 20% at 75% 90%, var(--flame-yellow), transparent 70%),
      radial-gradient(ellipse 70% 25% at 80% 15%, rgba(232,50,26,.8), transparent 70%),
      linear-gradient(90deg, transparent 0%, rgba(232,50,26,.25) 60%, rgba(247,130,30,.55) 100%);
  }
  .tube--side .flame--burst {
    left: 0; top: 16px; width: 384px; height: 420px;
    background:
      radial-gradient(ellipse 40% 35% at 20% 30%, var(--flame-yellow), transparent 70%),
      radial-gradient(ellipse 75% 55% at 45% 20%, rgba(247,130,30,.85), transparent 70%),
      radial-gradient(ellipse 90% 70% at 60% 30%, rgba(232,50,26,.6), transparent 75%);
  }
  .tube--side .flame--edge {
    right: 0; top: 300px; width: 140px; height: 606px;
    background: linear-gradient(90deg, transparent, rgba(232,50,26,.35) 60%, rgba(232,50,26,.6));
  }

  .brand { color: var(--text); font-weight: 300; line-height: 1; }
  .details { color: var(--text); font-weight: 400; font-size: 15px; letter-spacing: .5px; line-height: 1.25; }
  .size { color: var(--text); font-size: 13px; letter-spacing: 1px; }

  .label-front { position: absolute; left: 106px; top: 576px; }
  .label-front .brand { font-size: 50px; }
  .label-front .details { margin-top: 14px; }
  .label-front .size { margin-top: 22px; }

  .label-side {
    position: absolute; left: 150px; width: 140px; top: 532px;
    display: flex; flex-direction: column; align-items: center; text-align: center;
  }
  .label-side .brand {
    display: flex; flex-direction: column; align-items: center;
    font-size: 46px; gap: 0;
  }
  .label-side .brand span { display: block; height: 44px; }
  .label-side .details { margin-top: 22px; }
  .label-side .size { margin-top: 24px; }
</style>
</head>
<body>
<main class="canvas">
  <section class="tube tube--front">
    <div class="crimp"></div>
    <div class="flame flame--edge" role="img" aria-label="Abstract red and orange flame wisps along the right edge"></div>
    <div class="label-front">
      <p class="brand">Kalvio</p>
      <p class="details">BURN CREAM<br>LIDOCAINE 2.5%</p>
      <p class="size">1 OZ</p>
    </div>
    <div class="silver-band"></div>
    <div class="cap"></div>
  </section>

  <section class="tube tube--side">
    <div class="crimp"></div>
    <div class="flame flame--burst" role="img" aria-label="Burst of orange and yellow flame wisps across the top"></div>
    <div class="flame flame--edge" role="img" aria-label="Red flame wisps running down the right edge"></div>
    <div class="label-side">
      <p class="brand" aria-label="Kalvio"><span>K</span><span>a</span><span>l</span><span>v</span><span>i</span><span>o</span></p>
      <p class="details">BURN CREAM<br>LIDOCAINE 2.5%</p>
      <p class="size">1 OZ</p>
    </div>
    <div class="silver-band"></div>
    <div class="cap"></div>
  </section>
</main>
</body>
</html>
```